Letterhead and email signiture

Hello,

I have an example of a letterhead that we need. The one we have constandly moves if we paste any information in it. We are looking for one that is permanent. We only need the top of the letterhead on the first page but the bottom on each and every page afterward.

It does not have to be exactly what I am providing here. Please take a look at the website and maybe you will have a better idea.

We are looking to do something similar for an email signature

Maplerockllc.com

```html
<!DOCTYPE html>
<html lang="en">
<head>
<meta charset="utf-8">
<title>Maple Rock LLC – Letterhead and Business Card</title>
<link href="https://fonts.googleapis.com/css2?family=Montserrat:wght@700&family=Arimo:wght@400&family=Roboto:wght@400;700&display=swap" rel="stylesheet">
<style>
  :root{
    --backdrop:#bcbcbc;
    --paper:#ffffff;
    --ink:#1a1a1a;
    --body-text:#4a4a4a;
    --band:#171717;
    --brand-blue:#3f88d3;
    --shadow:rgba(0,0,0,.35);
  }
  *{margin:0;padding:0;box-sizing:border-box}
  html,body{width:884px;height:1200px;overflow:hidden;background:var(--backdrop)}
  body{position:relative;font-family:"Arimo",Arial,sans-serif}

  .sheet{position:absolute;background:var(--paper);box-shadow:3px 3px 5px var(--shadow)}

  /* Letterhead */
  .letterhead{left:160px;top:41px;width:565px;height:800px}
  .wordmark{position:absolute;font-family:"Montserrat",Arial,sans-serif;font-weight:700;color:var(--ink);letter-spacing:-.5px;white-space:nowrap;line-height:1}
  .letterhead .wordmark{left:37px;top:34px;font-size:21px}
  .salutation{position:absolute;left:51px;top:247px;font-size:13px;color:var(--body-text)}
  .letter-body{position:absolute;left:50px;top:284px;width:464px;font-size:9.3px;line-height:11.6px;color:var(--body-text)}
  .letter-body p{margin-bottom:10px}
  .closing{position:absolute;left:51px;top:523px;font-size:7px;color:var(--body-text)}
  .signature{position:absolute;left:43px;top:553px;width:78px;height:16px;background:linear-gradient(90deg,#d9d9d9,#eeeeee);border-radius:3px}

  .footer-band{position:absolute;left:0;top:750px;width:100%;height:37px}
  .footer-band .dark{position:absolute;left:0;top:0;bottom:0;width:470px;background:var(--band)}
  .footer-band .accent{position:absolute;right:0;top:0;bottom:0;width:95px;background:var(--brand-blue)}
  .footer-band .seal{position:absolute;left:467px;top:-5px;width:47px;height:47px;border-radius:50%;background:var(--brand-blue);border:5px solid var(--paper)}
  .footer-text{position:absolute;left:26px;top:5px;color:#fff;font-size:8.8px;line-height:13px}
  .contact-row{display:flex;align-items:center;gap:4px;white-space:nowrap}
  .contact-row .gap{width:6px}
  .icon{fill:var(--brand-blue);flex:none}

  /* Business card */
  .card{left:139px;top:879px;width:607px;height:243px;font-family:"Roboto",Arial,sans-serif}
  .card .wordmark{left:24px;top:29px;font-size:34px}
  .person-name{position:absolute;left:25px;top:78px;font-size:22px;font-weight:700;color:var(--brand-blue);letter-spacing:.2px}
  .person-role{position:absolute;left:25px;top:103px;font-size:16.5px;color:#555}
  .card .contact-row{position:absolute;left:25px;top:135px;font-size:15px;color:#555;gap:5px}
  .card .contact-row .gap{width:10px}
  .card-band{position:absolute;left:0;top:164px;width:100%;height:62px}
  .card-band .dark{position:absolute;left:0;top:0;bottom:0;width:500px;background:var(--band)}
  .card-band .accent{position:absolute;right:0;top:0;bottom:0;width:90px;background:var(--brand-blue)}
  .card-band .seal{position:absolute;left:489px;top:-8px;width:78px;height:78px;border-radius:50%;background:var(--brand-blue);border:7px solid var(--paper)}
  .card-band .notice{position:absolute;left:25px;top:11px;color:#fff;font-size:15px;line-height:19px}
</style>
</head>
<body>

<section class="sheet letterhead">
  <div class="wordmark">MAPLEROCK LLC</div>

  <p class="salutation">Dear Mr. Carter,</p>

  <div class="letter-body">
    <p>Lorem ipsum dolor sit amet, consectetuer adipiscing elit, sed diam nonmmy nibh euismod tincidunt ut laor eet dolore magna aliquam erat volutpat. Ut wisi enim ad minim veniam, quis nostrud exerci tationmcorper suscipit lobortis nisl ut aliquip ex ea commodo consequat. Duis autem vel eum iriure dolor in hendrerit in vulputate velit esse molestie consequat, vel illum dolore eu feugiat</p>
    <p>Rorem ipsum dolor sit amet, consectetuer adipiscing elit, sed diam nonmmy nibh euismod tincidunt ut laor eet dolore magna aliquam erat volutpat. Ut wisi enim ad minim veniam, quis nostrud exerci tationmcorper suscipit lobortis nisl ut aliquip ex ea commodo consequat. Duis autem vel eum iriure dolor in hendrerit in vulputate velit esse molest</p>
    <p>Dorem ipsum dolor sit amet, consectetuer adipiscing elit, sed diam nonmmy nibh euismod tincidunt ut laor eet dolore magna aliquam erat volutpat. Ut wisi enim ad minim veniam, quis nostrud exerci tationmcorper suscipit lobortis nisl ut aliquip ex ea commodo consequat. Duis autem vel eum iriure dolor in hendrerit in suscipit lobortis nisl ut aliquip ex ea commodo consequat. Duis autem vel eum iriure dolor in hendrerit in vulputate velit esse molestie consequat, vel illum</p>
    <p>Sorem ipsum dolor sit amet, consectetuer adipiscing elit, sed diam nonmmy nibh euismod tincidunt ut laor eet dolore magna aliquam erat volutpat. Ut wisi enim ad minim veniam, quis nostrud exerci tationmcorper suscipit lobortis nisl ut aliquip ex ea commodo consequat. Duis autem vel eum iriure dolor in</p>
  </div>

  <p class="closing">Sincerely,</p>
  <div class="signature" role="img" aria-label="Handwritten signature of Owen Hale"></div>

  <footer class="footer-band">
    <div class="dark"></div>
    <div class="accent"></div>
    <div class="seal"></div>
    <div class="footer-text">
      <div class="contact-row">
        <svg class="icon" width="9" height="8" viewBox="0 0 16 14"><path d="M1 4c0-2 3-3 7-3s7 1 7 3v2h-4V4.5H5V6H1z M4 7h8l2 6H2z"/></svg>
        <span>555-803-0100</span><span class="gap"></span>
        <svg class="icon" width="9" height="8" viewBox="0 0 16 14"><path d="M1 4c0-2 3-3 7-3s7 1 7 3v2h-4V4.5H5V6H1z M4 7h8l2 6H2z"/></svg>
        <span>555-530-0200</span><span class="gap"></span>
        <svg class="icon" width="9" height="9" viewBox="0 0 16 16"><circle cx="8" cy="8" r="7"/><path d="M1 8h14M8 1c3 3 3 11 0 14M8 1c-3 3-3 11 0 14" stroke="#171717" stroke-width="1.2" fill="none"/></svg>
        <span>MAPLEROCKLLC.COM</span>
      </div>
      <div>This document is confidential and intended solely for investigative purposes by Maple Rock LLC.</div>
    </div>
  </footer>
</section>

<section class="sheet card">
  <div class="wordmark">MAPLEROCK LLC</div>
  <div class="person-name">DANIEL CARTER</div>
  <div class="person-role">Manager</div>
  <div class="contact-row">
    <svg class="icon" width="16" height="14" viewBox="0 0 16 14"><path d="M1 4c0-2 3-3 7-3s7 1 7 3v2h-4V4.5H5V6H1z M4 7h8l2 6H2z"/></svg>
    <span>555-803-0100</span><span class="gap"></span>
    <svg class="icon" width="16" height="14" viewBox="0 0 16 14"><path d="M1 4c0-2 3-3 7-3s7 1 7 3v2h-4V4.5H5V6H1z M4 7h8l2 6H2z"/></svg>
    <span class="gap"></span><span>555-530-0200</span><span class="gap"></span>
    <svg class="icon" width="15" height="15" viewBox="0 0 16 16"><circle cx="8" cy="8" r="7"/><path d="M1 8h14M8 1c3 3 3 11 0 14M8 1c-3 3-3 11 0 14" stroke="#fff" stroke-width="1.2" fill="none"/></svg>
    <span class="gap"></span><span>MAPLEROCKLLC.COM</span>
  </div>
  <div class="card-band">
    <div class="dark"></div>
    <div class="accent"></div>
    <div class="seal"></div>
    <p class="notice">This document is confidential and<br>intended solely for investigative purposes by Maple Rock LLC.</p>
  </div>
</section>

</body>
</html>
```